Vintage themed home decor Shopify store needs sales promotion banner ads

"Quill & Lantern Goods" is an Australian based lifestyle home decor store that sells vintage, retro and antique relic replicas and reproduction items online to their local customers Australia wide.

We need banner ads for our store home page slider that promotes our unique products, new stock arrival and calls store visitors to to buy from our different product collections.

We anticipate that we will need multiple banner ads, primarily for the following product collections:
1. Sundials & Compass
2. Airplane models
3. Magnifying glass
4. Clocks & Watches

Banners could also be generic with generic discount coupon promotions.

Banners should be based around the theme of our store and products which gives a sense of colonial / vintage lifestyle and that they compliment the colour & theme of the store.

Banner Size: 1600 x 800 px

Please find attached some samples of the types of banner ads we have in mind and also our logo. Product images can be supplied if they are required to be used in the ads.

Website URL: https://quillandlanterngoods.example

Target Market(s)

mostly Males aged between 35-65.
Products ideally for man-cave & office decor.

Industry/Entity Type

Home And Garden

Font styles to use
Serif
Decorative
Script

Requirements
Must have
• some product images
Nice to have
• lifestyle shots.
• blank space to insert for a coupon code
Should not have
• caricatures & cartoon

```html
<!DOCTYPE html>
<html lang="en">
<head>
<meta charset="utf-8">
<title>Quill &amp; Lantern Goods — Collection Banners</title>
<link rel="stylesheet" href="https://fonts.googleapis.com/css2?family=Arvo:wght@400;700&family=Lato:wght@400;700&display=swap">
<style>
  :root {
    --page: #ffffff;
    --banner-bg: #f3f3f4;
    --banner-rule: #b9b9bb;
    --ink: #262626;
    --ink-soft: #4a4a4a;
    --ribbon: #f26522;
    --ribbon-line: #f7955f;
    --button: #2a2a2a;
    --button-line: #8c8c8c;
    --on-dark: #ffffff;
  }
  * { margin: 0; padding: 0; box-sizing: border-box; }
  html, body {
    width: 945px; height: 1200px; overflow: hidden;
    background: var(--page);
  }
  .banner-stack { position: relative; width: 945px; height: 1200px; }
  .banner {
    position: absolute; left: 196px; width: 553px; height: 270px;
    background: linear-gradient(180deg, #f6f6f7 0%, var(--banner-bg) 100%);
    border-top: 1px solid var(--banner-rule);
    border-bottom: 1px solid var(--banner-rule);
    box-shadow: 0 6px 10px rgba(0,0,0,0.12);
    overflow: hidden;
  }
  .banner--magnifier { top: 12px; }
  .banner--aeroplane { top: 307px; }
  .banner--compass { top: 608px; }
  .banner--clocks { top: 909px; }

  .banner__title {
    position: absolute; top: 68px;
    font-family: "Arvo", serif; font-weight: 400; font-size: 19px;
    letter-spacing: 3.6px; color: var(--ink); white-space: nowrap;
  }
  .banner__blurb {
    position: absolute; top: 96px;
    font-family: "Lato", sans-serif; font-size: 8.6px; line-height: 10.5px;
    letter-spacing: 0.9px; color: var(--ink-soft); white-space: nowrap;
  }
  .ribbon { position: absolute; top: 129px; width: 289px; height: 44px; }
  .ribbon svg { position: absolute; inset: 0; }
  .ribbon__label {
    position: absolute; top: 10px; width: 100%; text-align: center;
    font-family: "Lato", sans-serif; font-size: 6.5px; letter-spacing: 1px;
    color: var(--on-dark);
  }
  .ribbon__code {
    position: absolute; top: 17px; width: 100%; text-align: center;
    font-family: "Arvo", serif; font-weight: 700; font-size: 14px;
    letter-spacing: 1.6px; color: var(--on-dark);
  }
  .shop-button {
    position: absolute; top: 197px; width: 157px; height: 34px;
    background: var(--button); color: var(--on-dark);
    font-family: "Lato", sans-serif; font-size: 14px; letter-spacing: 2.6px;
    display: flex; align-items: center; justify-content: center;
    text-decoration: none;
  }
  .shop-button::before, .shop-button::after {
    content: ""; position: absolute; left: 0; right: 0; height: 1px;
    background: var(--button-line);
  }
  .shop-button::before { top: 3px; }
  .shop-button::after { bottom: 3px; }

  /* text on the left */
  .banner--left .banner__title, .banner--left .banner__blurb { left: 14px; }
  .banner--left .ribbon { left: 0; }
  .banner--left .shop-button { left: 50px; }
  .banner--left .ribbon__label, .banner--left .ribbon__code { left: -18px; }

  /* text on the right */
  .banner--right .banner__title, .banner--right .banner__blurb { right: 12px; text-align: right; }
  .banner--right .ribbon { right: 0; }
  .banner--right .shop-button { left: 330px; }
  .banner--right .ribbon__label, .banner--right .ribbon__code { left: 18px; }

  .product-shot { position: absolute; }
  .product-shot--magnifier {
    left: 300px; top: 22px; width: 226px; height: 242px;
    background: radial-gradient(ellipse at 40% 40%, #c9d3cf 0%, #8a7a5a 45%, #5a3a26 100%);
    border-radius: 40% 50% 30% 30%; opacity: 0.85;
  }
  .product-shot--aeroplane {
    left: 0; top: 95px; width: 296px; height: 100px;
    background: linear-gradient(170deg, #e6c23a 0%, #c99a20 55%, #5a5a60 100%);
    border-radius: 30% 10% 30% 20%; opacity: 0.85;
  }
  .product-shot--compass {
    left: 41px; top: 38px; width: 217px; height: 228px;
    background: linear-gradient(150deg, #6b4a32 0%, #8a6a44 45%, #3a3530 100%);
    border-radius: 20% 40% 10% 30%; opacity: 0.85;
  }
  .product-shot--clock {
    left: 333px; top: 50px; width: 176px; height: 176px; border-radius: 50%;
    background: radial-gradient(circle, #8a6a40 0%, #8a6a40 25%, #f1efe9 27%, #efece4 80%, #a87440 84%, #c9965a 100%);
  }
</style>
</head>
<body>
<main class="banner-stack">

  <section class="banner banner--left banner--magnifier">
    <div class="product-shot product-shot--magnifier" role="img" aria-label="Antique brass magnifying glass on a wooden stand"></div>
    <h2 class="banner__title">MAGNIFYING GLASS</h2>
    <p class="banner__blurb">Lorem ipsum dolor sit amet, consectetur<br>adipisicing elit, sed do eiusmod tempor inc-</p>
    <div class="ribbon">
      <svg width="289" height="44" viewBox="0 0 289 44"><polygon points="0,0 289,0 260,22 289,44 0,44" fill="var(--ribbon)"/><polyline points="0,3 280,3 256,22 280,41 0,41" fill="none" stroke="var(--ribbon-line)" stroke-width="0.8"/></svg>
      <span class="ribbon__label">SPECIAL OFFER COUPON CODE</span>
      <span class="ribbon__code">AIYPWZQP</span>
    </div>
    <a class="shop-button" href="https://quillandlanterngoods.example">SHOP NOW</a>
  </section>

  <section class="banner banner--right banner--aeroplane">
    <div class="product-shot product-shot--aeroplane" role="img" aria-label="Yellow vintage biplane model"></div>
    <h2 class="banner__title">AEROPLANE MODELS</h2>
    <p class="banner__blurb">Lorem ipsum dolor sit amet, consectetur<br>adipisicing elit, sed do eiusmod tempor inc-</p>
    <div class="ribbon">
      <svg width="289" height="44" viewBox="0 0 289 44"><polygon points="0,0 289,0 289,44 0,44 29,22" fill="var(--ribbon)"/><polyline points="289,3 9,3 33,22 9,41 289,41" fill="none" stroke="var(--ribbon-line)" stroke-width="0.8"/></svg>
      <span class="ribbon__label">SPECIAL OFFER COUPON CODE</span>
      <span class="ribbon__code">AIYPWZQP</span>
    </div>
    <a class="shop-button" href="https://quillandlanterngoods.example">SHOP NOW</a>
  </section>

  <section class="banner banner--right banner--compass">
    <div class="product-shot product-shot--compass" role="img" aria-label="Boxed brass sundial and a gimballed compass on a stand"></div>
    <h2 class="banner__title">SUNDIALS &amp; COMPASS</h2>
    <p class="banner__blurb">Lorem ipsum dolor sit amet, consectetur<br>adipisicing elit, sed do eiusmod tempor inc-</p>
    <div class="ribbon">
      <svg width="289" height="44" viewBox="0 0 289 44"><polygon points="0,0 289,0 289,44 0,44 29,22" fill="var(--ribbon)"/><polyline points="289,3 9,3 33,22 9,41 289,41" fill="none" stroke="var(--ribbon-line)" stroke-width="0.8"/></svg>
      <span class="ribbon__label">SPECIAL OFFER COUPON CODE</span>
      <span class="ribbon__code">AIYPWZQP</span>
    </div>
    <a class="shop-button" href="https://quillandlanterngoods.example">SHOP NOW</a>
  </section>

  <section class="banner banner--left banner--clocks">
    <div class="product-shot product-shot--clock" role="img" aria-label="Round wall clock with exposed gear centre"></div>
    <h2 class="banner__title">CLOCKS &amp; WATCHES</h2>
    <p class="banner__blurb">Lorem ipsum dolor sit amet, consectetur<br>adipisicing elit, sed do eiusmod tempor inc-</p>
    <div class="ribbon">
      <svg width="289" height="44" viewBox="0 0 289 44"><polygon points="0,0 289,0 260,22 289,44 0,44" fill="var(--ribbon)"/><polyline points="0,3 280,3 256,22 280,41 0,41" fill="none" stroke="var(--ribbon-line)" stroke-width="0.8"/></svg>
      <span class="ribbon__label">SPECIAL OFFER COUPON CODE</span>
      <span class="ribbon__code">AIYPWZQP</span>
    </div>
    <a class="shop-button" href="https://quillandlanterngoods.example">SHOP NOW</a>
  </section>

</main>
</body>
</html>
```